Refresh Brightwave Coursecraft

Need a new design for e-learning development and web app development site: http://brightwavecoursecraft.example. Need pages for everything on menu bar plus a training services and a web app development services pages and a better page for samples http://brightwavecoursecraft.example/samples5/.

***Must be programmed in html 5. NO CMS. No WP. No Pillar. Straight html/css.

Target Market(s)

government

Industry/Entity Type

Government

Coding

Coded - Design and coding required

Number of Pages Required

1 page

Requirements
Must have
• Must be coded in html5/css. No CMS.
• Divided so you can easily see that we offer 3 separate services:
• Live Training - E-Learning Development - Web App Development
• A way to display logos of all our clients like on bottom of this page: https://www.quorvatests.example (this is also our website so you can copy all these logos)
• List both our Denver location which is already on our website plus our office in Veltoma Plaza. Street 62 Este, 17-83. Medellín, Antioquia.
• A page like this for our web app dev services https://www.zelbrax.example/product-development
Should not have
• CMS

```html
<!DOCTYPE html>
<html lang="en">
<head>
<meta charset="utf-8">
<title>Brightwave Coursecraft</title>
<link href="https://fonts.googleapis.com/css2?family=Roboto:wght@300;400;500;700&family=Roboto+Condensed:wght@400;700&display=swap" rel="stylesheet">
<style>
:root{
  --orange:#f7941d;
  --orange-dark:#e9800a;
  --navy:#0f2a4a;
  --blue:#143f70;
  --blue-deep:#0b2748;
  --ink:#333a44;
  --muted:#7a7f87;
  --line:#dcdfe3;
  --light:#f2f2f2;
  --white:#ffffff;
}
*{box-sizing:border-box;margin:0;padding:0}
html,body{width:1200px;height:3068px;overflow:hidden}
body{font-family:"Roboto",sans-serif;color:var(--ink);background:var(--white)}
section,header,footer{position:relative;width:1200px;overflow:hidden}

/* header */
.site-header{height:88px;background:var(--white);box-shadow:0 2px 6px rgba(0,0,0,.08);z-index:2}
.brand{position:absolute;left:0;top:0;height:88px;width:330px;background:var(--orange);display:flex;align-items:center;padding-left:28px;gap:14px;clip-path:polygon(0 0,100% 0,88% 100%,0 100%)}
.brand-mark{width:44px;height:44px;border-radius:50%;background:var(--white)}
.brand-name{font-family:"Roboto Condensed",sans-serif;font-weight:700;color:var(--white);font-size:20px;letter-spacing:1px;line-height:1.1}
.main-nav{position:absolute;right:40px;top:0;height:88px;display:flex;align-items:center;gap:38px}
.main-nav a{font-size:13px;font-weight:500;color:var(--ink);text-decoration:none;letter-spacing:.5px}
.main-nav a.active{color:var(--orange)}

/* hero */
.hero{height:632px}
.hero-photo{position:absolute;inset:0;background:radial-gradient(ellipse at 65% 45%,#2f6fb0 0%,#15437a 45%,#071a36 100%)}
.hero-copy{position:absolute;left:0;right:0;top:250px;text-align:center;color:var(--white)}
.hero-kicker{font-size:34px;font-weight:300}
.hero-title{display:inline-block;margin-top:8px;font-family:"Roboto Condensed",sans-serif;font-size:78px;font-weight:400;letter-spacing:2px;padding:0 24px}

/* about */
.about{height:560px;background:var(--light)}
.about-visual{position:absolute;left:0;top:0;width:600px;height:560px;background:linear-gradient(135deg,#e8e8e8,#cfd3d6)}
.about-copy{position:absolute;left:640px;top:90px;width:500px}
.about-eyebrow{font-family:"Roboto Condensed",sans-serif;font-weight:700;font-size:23px;color:var(--navy)}
.about-title{font-family:"Roboto Condensed",sans-serif;font-weight:700;font-size:50px;color:var(--orange);line-height:1.05;margin-top:4px}
.about-text{font-size:13px;line-height:1.75;color:var(--muted);margin-top:22px}
.btn-outline{display:inline-block;margin-top:26px;border:2px solid var(--orange);color:var(--navy);font-size:11px;font-weight:700;padding:8px 18px;letter-spacing:.5px}

/* services */
.services{height:620px;text-align:center}
.section-title{font-family:"Roboto Condensed",sans-serif;font-weight:700;font-size:40px;color:var(--orange);padding-top:70px}
.title-rule{width:80px;height:2px;background:var(--orange);margin:12px auto 0}
.section-intro{width:560px;margin:26px auto 0;font-size:13px;line-height:1.7;color:var(--muted)}
.service-cards{position:absolute;left:32px;top:260px;display:flex;gap:32px}
.service-card{width:356px;height:300px;border:1px solid var(--line);background:var(--white);padding:34px 32px}
.service-card.featured{border:2px solid var(--orange)}
.service-icon{width:56px;height:56px;margin:0 auto}
.service-name{font-size:25px;color:var(--ink);margin-top:22px}
.service-card.featured .service-name{color:var(--orange);font-weight:500}
.service-text{font-size:13px;line-height:1.7;color:var(--muted);margin-top:16px}

/* call to action */
.cta{height:112px;background:var(--orange);display:flex;align-items:center;padding:0 80px;justify-content:space-between}
.cta-text{font-size:34px;font-weight:300;color:var(--white)}
.cta-text strong{font-weight:700}
.btn-solid-white{background:var(--white);color:var(--navy);font-weight:700;font-size:14px;padding:12px 26px}

/* clients */
.clients{height:460px;text-align:center}
.clients-title{font-size:30px;font-weight:400;color:var(--ink);padding-top:40px}
.client-row{display:flex;justify-content:center;align-items:center;gap:34px;margin-top:38px}
.client{display:flex;align-items:center;gap:8px;font-size:17px;font-weight:700;color:var(--navy)}
.client-dot{width:30px;height:30px;border-radius:50%;background:var(--blue)}
.client-seal{width:78px;height:78px;border-radius:50%;background:#c9b27a}
.client-seal.red{background:#b33a3a}
.client-seal.navy{background:var(--navy)}
.client-seal.gold{background:#d9a62c}

/* footer */
.site-footer{height:518px;background:linear-gradient(160deg,var(--blue) 0%,var(--blue-deep) 100%);color:var(--white)}
.footer-col{position:absolute;top:80px}
.footer-col.touch{left:70px;width:470px}
.footer-col.contacts{left:740px;width:400px}
.footer-heading{font-size:34px;font-weight:500;letter-spacing:.5px}
.footer-rule{width:100%;height:1px;background:rgba(255,255,255,.35);margin-top:14px}
.footer-text{font-size:13px;line-height:1.7;color:#c5d2e2;margin-top:18px}
.form-row{display:flex;gap:30px;margin-top:34px}
.field{flex:1;border-bottom:1px solid rgba(255,255,255,.45);font-size:11px;color:#c5d2e2;padding-bottom:10px}
.btn-submit{display:inline-block;margin-top:34px;background:var(--orange);font-size:12px;font-weight:700;padding:10px 30px}
.contact-line{display:flex;align-items:center;gap:16px;margin-top:24px;font-size:13px;color:#d6e0ec;line-height:1.5}
.contact-icon{width:26px;height:26px;flex:none}
.social{display:flex;gap:12px;margin-top:30px}
.social span{width:34px;height:34px;border-radius:50%;background:rgba(255,255,255,.25)}

.bottom-bar{height:78px;background:#e9eaec;display:flex;align-items:center;justify-content:space-between;padding:0 70px;font-size:12px;color:var(--muted)}
.bottom-links{display:flex;gap:36px}
</style>
</head>
<body>

<header class="site-header">
  <div class="brand"><span class="brand-mark"></span><span class="brand-name">BRIGHTWAVE<br>COURSECRAFT</span></div>
  <nav class="main-nav">
    <a class="active">HOME</a><a>SERVICES</a><a>PORTFOLIO</a><a>TEAMS &amp; EXPERIENCE</a><a>CONTACT</a>
  </nav>
</header>

<section class="hero">
  <div class="hero-photo" role="img" aria-label="Hands holding a tablet surrounded by glowing learning icons in blue light"></div>
  <div class="hero-copy">
    <p class="hero-kicker">We create engaging training that exceed</p>
    <h1 class="hero-title">EXPECTATIONS</h1>
  </div>
</section>

<section class="about">
  <div class="about-visual" role="img" aria-label="Laptop on a desk showing an e-learning illustration"></div>
  <div class="about-copy">
    <h2 class="about-eyebrow">AN INSTRUCTIONAL DESIGN &amp; COURSEWARE</h2>
    <p class="about-title">DEVELOPMENT FIRM</p>
    <p class="about-text">Brightwave Coursecraft is a certified small business and service-disabled veteran-owned firm based in Denver, Colorado. We have designed and delivered SCORM compliant eLearning, webinar, web-based training, instructor-led training, virtual ILT, blended, and 3D immersive training courses. The instructional design team brings nearly one hundred years of combined design experience. Our instructional designers have experience designing, developing, and delivering custom technical and business training courses.</p>
    <span class="btn-outline">READ MORE</span>
  </div>
</section>

<section class="services">
  <h2 class="section-title">OUR BEST SERVICES</h2>
  <div class="title-rule"></div>
  <p class="section-intro">Lorem ipsum dolor sit amet, consectetur adipiscing elit. Fusce aliquet, massa ac ornare feugiat, nunc dui auctor ipsum, sed posuere eros sapien id quam.</p>
  <div class="service-cards">
    <article class="service-card featured">
      <svg class="service-icon" viewBox="0 0 56 56"><rect x="6" y="8" width="44" height="30" rx="2" fill="none" stroke="#0f2a4a" stroke-width="3"/><circle cx="28" cy="20" r="5" fill="#f7941d"/><path d="M19 34c2-6 16-6 18 0" fill="#f7941d"/><path d="M22 46h12M28 38v8" stroke="#0f2a4a" stroke-width="3"/></svg>
      <h3 class="service-name">Live Training</h3>
      <p class="service-text">Lorem ipsum dolor sit amet, consectetur adipiscing elit. Fusce aliquet, massa ac ornare feugiat, nunc dui auctor ipsum.</p>
    </article>
    <article class="service-card">
      <svg class="service-icon" viewBox="0 0 56 56"><circle cx="28" cy="28" r="26" fill="#f7941d"/><circle cx="28" cy="24" r="9" fill="none" stroke="#fff" stroke-width="3"/><path d="M23 38h10M24 43h8" stroke="#fff" stroke-width="3"/></svg>
      <h3 class="service-name">E-Learning Development</h3>
      <p class="service-text">Lorem ipsum dolor sit amet, consectetur adipiscing elit. Fusce aliquet, massa ac ornare feugiat, nunc dui auctor ipsum.</p>
    </article>
    <article class="service-card">
      <svg class="service-icon" viewBox="0 0 56 56"><rect x="10" y="12" width="36" height="24" rx="2" fill="none" stroke="#f7941d" stroke-width="3"/><path d="M4 42h48" stroke="#f7941d" stroke-width="4"/><path d="M22 22l-4 3 4 3M34 22l4 3-4 3" stroke="#0f2a4a" stroke-width="2" fill="none"/></svg>
      <h3 class="service-name">Web App Development</h3>
      <p class="service-text">Lorem ipsum dolor sit amet, consectetur adipiscing elit. Fusce aliquet, massa ac ornare feugiat, nunc dui auctor ipsum.</p>
    </article>
  </div>
</section>

<section class="cta">
  <p class="cta-text">Looking for a quality <strong>e-learning service</strong>?</p>
  <span class="btn-solid-white">CONTACT US</span>
</section>

<section class="clients">
  <h2 class="clients-title">A Few Of Our 75,000 Clients</h2>
  <div class="client-row">
    <span class="client"><span class="client-dot"></span>Northvale Air Wing</span>
    <span class="client-seal navy"></span>
    <span class="client-seal gold"></span>
    <span class="client-seal red"></span>
    <span class="client-seal"></span>
    <span class="client"><span class="client-dot"></span>Pellium</span>
    <span class="client"><span class="client-dot"></span>Veridane</span>
  </div>
  <div class="client-row">
    <span class="client-seal"></span>
    <span class="client"><span class="client-dot"></span>Marrow Institute</span>
    <span class="client-seal gold"></span>
    <span class="client"><span class="client-dot"></span>University of Halbrook</span>
    <span class="client"><span class="client-dot"></span>Osteline</span>
    <span class="client-seal navy"></span>
    <span class="client-seal red"></span>
  </div>
  <div class="client-row">
    <span class="client"><span class="client-dot"></span>Corran University</span>
    <span class="client"><span class="client-dot"></span>Kestrel State</span>
    <span class="client"><span class="client-dot"></span>Ridgeline University</span>
    <span class="client-seal gold"></span>
    <span class="client-seal red"></span>
    <span class="client"><span class="client-dot"></span>Tavix</span>
  </div>
</section>

<footer class="site-footer">
  <div class="footer-col touch">
    <h2 class="footer-heading">GET IN TOUCH</h2>
    <div class="footer-rule"></div>
    <p class="footer-text">Lorem ipsum dolor sit amet, consectetur adipiscing elit. Fusce aliquet, massa ac ornare feugiat, nunc dui auctor ipsum.</p>
    <div class="form-row"><span class="field">NAME</span><span class="field">EMAIL</span></div>
    <div class="form-row"><span class="field" style="padding-bottom:60px">MESSAGE</span></div>
    <span class="btn-submit">SUBMIT</span>
  </div>
  <div class="footer-col contacts">
    <h2 class="footer-heading">CONTACTS</h2>
    <div class="footer-rule"></div>
    <div class="contact-line">
      <svg class="contact-icon" viewBox="0 0 26 26"><path d="M13 2a8 8 0 0 0-8 8c0 6 8 14 8 14s8-8 8-14a8 8 0 0 0-8-8z" fill="#fff"/><circle cx="13" cy="10" r="3" fill="#143f70"/></svg>
      <span>2280 Larkspur Avenue, Suite 410<br>Aurora, CO 80014</span>
    </div>
    <div class="contact-line">
      <svg class="contact-icon" viewBox="0 0 26 26"><path d="M7 3l4 5-2 3c1 3 3 5 6 6l3-2 5 4-3 4C11 23 3 15 3 6z" fill="#fff"/></svg>
      <span>+1 800 555 0142</span>
    </div>
    <div class="contact-line">
      <svg class="contact-icon" viewBox="0 0 26 26"><rect x="3" y="6" width="20" height="14" rx="1" fill="#fff"/><path d="M3 7l10 7 10-7" stroke="#143f70" stroke-width="1.5" fill="none"/></svg>
      <span>support@brightwavecoursecraft.example</span>
    </div>
    <div class="social" aria-label="Social profiles"><span></span><span></span><span></span><span></span><span></span></div>
  </div>
</footer>

<div class="bottom-bar">
  <span>Copyright 2018 Brightwave Coursecraft. All Rights Reserved.</span>
  <span class="bottom-links"><span>Sitemap</span><span>Terms of Service</span><span>Privacy Policy</span></span>
</div>

</body>
</html>
```